I am a general contractor in Portland, Or. I would like a clean and simple design layout, maybe using the "didot" font, blue and dark bronze in colors are preferred. On one side of the card, it would be nice to have a logo(attached photo) and business name(KBT Construction). I don't need my job title on the card, just some thing along the lines of "harold pike, general contractor". Thanks much.

Target Market(s)

Adults from 30-55 years old. Middle to upper class.

Industry/Entity Type

Contractor

Contact Information for Business Card

KBT Construction
Harold M. Pike
2943 NE 71st Ave.
Portland, Or. 97288
503.627.9184

Font styles to use
Other font styles liked:
• didot

Colors
3277b5
7f7f7f

Requirements
Should not have
• Too much going on.

```html
<!DOCTYPE html>
<html lang="en">
<head>
<meta charset="utf-8">
<title>KBT Construction — Business Card</title>
<link rel="stylesheet" href="https://fonts.googleapis.com/css2?family=GFS+Didot&family=Arimo:wght@400;700&display=swap">
<style>
  :root {
    --backdrop: #ebebeb;
    --card: #ffffff;
    --brand-blue: #3277b5;
    --brand-grey: #7f7f7f;
    --serif: "GFS Didot", "Didot", serif;
    --sans: "Arimo", "Helvetica Neue", Arial, sans-serif;
  }
  * { box-sizing: border-box; margin: 0; padding: 0; }
  html, body {
    width: 1200px;
    height: 1000px;
    overflow: hidden;
    background: var(--backdrop);
  }
  .canvas {
    position: relative;
    width: 1200px;
    height: 1000px;
  }
  .card {
    position: absolute;
    width: 542px;
    height: 316px;
    background: var(--card);
  }
  .card--front { left: 155px; top: 145px; }
  .card--back  { left: 479px; top: 531px; }

  .brand-mark {
    position: absolute;
    display: block;
  }
  .brand-name {
    position: absolute;
    font-family: var(--serif);
    font-weight: 400;
    color: var(--brand-grey);
    letter-spacing: 0.04em;
    white-space: nowrap;
    line-height: 1;
  }
  .brand-tagline {
    position: absolute;
    font-family: var(--sans);
    color: var(--brand-grey);
    white-space: nowrap;
    line-height: 1;
  }

  /* Front: contact side */
  .card--front .brand-mark { left: 380px; top: 35px; }
  .card--front .brand-name { right: 27px; top: 104px; font-size: 22px; }
  .card--front .brand-tagline { right: 28px; top: 125px; font-size: 14px; }

  .contact {
    position: absolute;
    left: 30px;
    top: 174px;
  }
  .contact__name {
    font-family: var(--serif);
    font-weight: 400;
    font-size: 25px;
    color: var(--brand-blue);
    line-height: 1;
    margin-bottom: 14px;
  }
  .contact__line {
    font-family: var(--sans);
    font-size: 16px;
    color: var(--brand-grey);
    line-height: 25px;
  }
  .contact__company {
    font-weight: 700;
    font-size: 15px;
  }

  /* Back: logo side */
  .card--back .brand-mark { left: 235px; top: 70px; }
  .card--back .brand-name {
    left: 0; right: 0; top: 184px;
    text-align: center;
    font-size: 35px;
  }
  .card--back .brand-tagline {
    left: 0; right: 0; top: 221px;
    text-align: center;
    font-size: 21px;
  }
</style>
</head>
<body>
<main class="canvas">

  <section class="card card--front" aria-label="Business card, contact side">
    <svg class="brand-mark" width="54" height="54" viewBox="0 0 54 54" aria-hidden="true">
      <circle cx="27" cy="27" r="26" fill="#3277b5"/>
    </svg>
    <p class="brand-name">KBT CONSTRUCTION</p>
    <p class="brand-tagline">harold pike, general contractor</p>

    <address class="contact" style="font-style: normal;">
      <p class="contact__name">Harold M. Pike</p>
      <p class="contact__line contact__company">KBT CONSTRUCTION</p>
      <p class="contact__line">2943 NE 71st Ave. Portland, Or. 97288</p>
      <p class="contact__line">Mobile: 503.627.9184</p>
    </address>
  </section>

  <section class="card card--back" aria-label="Business card, logo side">
    <svg class="brand-mark" width="92" height="92" viewBox="0 0 92 92" aria-hidden="true">
      <circle cx="46" cy="46" r="45" fill="#3277b5"/>
    </svg>
    <p class="brand-name">KBT CONSTRUCTION</p>
    <p class="brand-tagline">harold pike, general contractor</p>
  </section>

</main>
</body>
</html>
```